Hollow Vectorfield by Gridvault records (digital cd cover artwork )

We running psytrance (psychedelic trance ) label records,
Our groove it's powerful abstract loaded with full of futurestic scifi sound and twisted mechanical texture.

So we looking for high quality 3d rendering abstract with futurestic twist, hud elements, plexus dark matter object.
It must be Sharp and cutting-edge.

Sure we respect out box thinking so feel free to add your ideas around that name concept.

Hollow Vectorfield

P.s
But the way
This is our whole thing concept
3d abstract, rendering object, dark matter
futurestic texture, scifi and hud elements,mechanical dark cutting-edge.
So if it's your flavor and you're love to work on that graphic design scale.

So we might want you with us.

Check out our releases artwork covers & music concept here.
https://gridvaultrecords.soundmesh.net/

And more from our freaky friends.
https://kirvamusic.soundmesh.net/

Thank you very much
Pavel

Gridvaultrecords@mailvine.net

Target Market(s)

Psytrance music

Industry/Entity Type

Music Download

Font styles to use
Serif

Colors

Designer to choose colors to be used in the design.

Requirements
Must have
• Album name: Hollow Vectorfield
• Label name: Gridvault Records
• Size cover: 3000 × 3000 pix
• Font design concept: technology, scifi or elegant
• Gridvault records logo or only Gridvault Records name on it
• Cutting edge
• Futurestic
• Dark matter/3d abstract render
Nice to have
• Plexus design (NOT A VIDEO. only the style concept )
• after effect
• Robotice
Should not have
• Old psychedelic colorful and retro style

```html
<!DOCTYPE html>
<html lang="en">
<head>
<meta charset="utf-8">
<title>Hollow Vectorfield — Gridvault Records</title>
<link rel="stylesheet" href="https://fonts.googleapis.com/css2?family=Rubik:wght@500;900&display=swap">
<style>
  :root {
    --bg-deep: #2a1511;
    --bg-mid: #3a1a12;
    --ember-hot: #d9521f;
    --ember-mid: #8e2f16;
    --ember-dark: #4a1a0e;
    --ember-band: #5e2414;
    --glow-mint: #b8f2c8;
    --glow-mint-shade: #8fd3a4;
    --core-blue: #6d78c8;
    --core-navy: #1d2138;
    --hud-line: #b8f2c8;
    --label-ink: #f3f2f6;
  }
  html, body {
    margin: 0;
    padding: 0;
    width: 1200px;
    height: 1200px;
    overflow: hidden;
    background: var(--bg-deep);
  }
  .cover {
    position: relative;
    width: 1200px;
    height: 1200px;
    background: radial-gradient(circle at 50% 45%, var(--bg-mid) 0%, var(--bg-deep) 70%);
  }
  .cover__art {
    position: absolute;
    inset: 0;
    width: 1200px;
    height: 1200px;
  }
  .cover__title {
    position: absolute;
    left: 0;
    right: 0;
    top: 1062px;
    margin: 0;
    text-align: center;
    font-family: "Rubik", "Arial", sans-serif;
    font-weight: 500;
    font-size: 22px;
    letter-spacing: 10px;
    line-height: 1;
    color: var(--glow-mint);
  }
  .cover__label {
    position: absolute;
    left: 0;
    right: 0;
    top: 1104px;
    margin: 0;
    text-align: center;
    font-family: "Rubik", "Arial Black", sans-serif;
    font-weight: 900;
    font-size: 64px;
    letter-spacing: 1px;
    line-height: 1;
    color: var(--label-ink);
  }
</style>
</head>
<body>
  <main class="cover">
    <svg class="cover__art" viewBox="0 0 1200 1200" xmlns="http://www.w3.org/2000/svg">
      <defs>
        <radialGradient id="emberGlow" cx="50%" cy="55%" r="60%">
          <stop offset="0%" stop-color="var(--ember-dark)"/>
          <stop offset="45%" stop-color="var(--ember-mid)"/>
          <stop offset="80%" stop-color="var(--ember-hot)"/>
          <stop offset="100%" stop-color="var(--ember-mid)"/>
        </radialGradient>
        <linearGradient id="coreGlow" x1="0" y1="0" x2="0" y2="1">
          <stop offset="0%" stop-color="var(--core-blue)"/>
          <stop offset="70%" stop-color="#3c4480"/>
          <stop offset="100%" stop-color="var(--core-navy)"/>
        </linearGradient>
      </defs>

      <g class="ember-tunnel" role="img"
        aria-label="Mirrored textured rock in glowing orange and rust tones forming a large triangular tunnel">
        <polygon points="600,0 1168,1040 40,1040" fill="url(#emberGlow)" opacity="0.92"/>
        <polygon points="598,110 1060,960 140,960" fill="none" stroke="var(--ember-band)" stroke-width="26" opacity="0.7"/>
        <polygon points="596,160 995,900 200,900" fill="none" stroke="var(--ember-hot)" stroke-width="8" opacity="0.45"/>
      </g>

      <g class="plexus" stroke="var(--hud-line)" stroke-width="1" opacity="0.35" fill="var(--hud-line)">
        <line x1="160" y1="880" x2="260" y2="700"/>
        <line x1="260" y1="700" x2="380" y2="470"/>
        <line x1="260" y1="700" x2="200" y2="960"/>
        <line x1="380" y1="470" x2="480" y2="260"/>
        <line x1="1040" y1="880" x2="940" y2="700"/>
        <line x1="940" y1="700" x2="820" y2="470"/>
        <line x1="940" y1="700" x2="1000" y2="960"/>
        <line x1="820" y1="470" x2="720" y2="260"/>
        <line x1="200" y1="960" x2="600" y2="990"/>
        <line x1="600" y1="990" x2="1000" y2="960"/>
        <circle cx="160" cy="880" r="3"/>
        <circle cx="260" cy="700" r="3"/>
        <circle cx="380" cy="470" r="3"/>
        <circle cx="480" cy="260" r="3"/>
        <circle cx="200" cy="960" r="3"/>
        <circle cx="1040" cy="880" r="3"/>
        <circle cx="940" cy="700" r="3"/>
        <circle cx="820" cy="470" r="3"/>
        <circle cx="720" cy="260" r="3"/>
        <circle cx="1000" cy="960" r="3"/>
        <circle cx="600" cy="990" r="3"/>
      </g>

      <polygon class="glow-frame" points="592,192 928,816 284,816" fill="var(--glow-mint)"/>
      <polygon class="glow-frame__inner" points="594,345 820,770 368,770" fill="var(--glow-mint-shade)" opacity="0.6"/>

      <polygon class="core-window" role="img"
        aria-label="Abstract close-up of blue and dark feathered texture inside the triangle"
        points="594,388 780,733 428,733" fill="url(#coreGlow)"/>

      <g class="hud" fill="none" stroke="var(--hud-line)" stroke-width="2" opacity="0.6">
        <polyline points="240,170 240,150 260,150"/>
        <polyline points="940,150 960,150 960,170"/>
        <polyline points="240,840 240,860 260,860"/>
        <polyline points="940,860 960,860 960,840"/>
        <line x1="594" y1="140" x2="594" y2="170"/>
        <line x1="594" y1="850" x2="594" y2="880"/>
      </g>
    </svg>

    <p class="cover__title">HOLLOW VECTORFIELD</p>
    <h1 class="cover__label">GRIDVAULT</h1>
  </main>
</body>
</html>
```